Uregent Care opening postcard with coupon

We need a postcard created to mail directly to homes. The flyer need to be appealing and include a small spot with a coupon for $20 gift card with first visit. The post card needs to be 2 sided and 4X6. We have a logo. To learn more about us visit maplegroveclinicplus.example or check us out on facebook. I will try to figure out how to upload logo.

Target Market(s)

All households that need urgent care.

Industry/Entity Type

Healthcare

Font styles to use
Serif

Colors
33a6d7
447fba
85acd3
85cae6
cfdfed
ecf7fb

Requirements
Must have
• our logo
• family centered
• some services offered
• coupon with free $20 gc at first visit if you bring in this flyer
Nice to have
• visually appealing

```html
<!DOCTYPE html>
<html lang="en">
<head>
<meta charset="utf-8">
<title>Maple Grove Clinic – Grand Opening Postcard</title>
<link rel="stylesheet" href="https://fonts.googleapis.com/css2?family=Oswald:wght@500;600;700&family=Lato:ital,wght@0,400;0,700;0,900;1,400;1,700&display=swap">
<style>
  :root{
    --navy:#1c1d5f;
    --blue:#3f6cb8;
    --blue-mid:#4a78c3;
    --blue-soft:#6f98d8;
    --grey-line:#9a9ea6;
    --paper:#ffffff;
    --stage:#e4e6ea;
  }
  *{margin:0;padding:0;box-sizing:border-box}
  html,body{width:902px;height:1200px;overflow:hidden;background:var(--stage)}
  body{position:relative;font-family:"Lato",Arial,sans-serif}
  .card{position:absolute;width:691px;height:470px;background:var(--paper);overflow:hidden;box-shadow:0 6px 18px rgba(0,0,0,.25)}
  .card--front{left:58px;top:101px}
  .card--back{left:121px;top:637px;width:690px;height:469px}
  .layer{position:absolute;left:0;top:0}

  .photo{position:absolute}
  .photo--exam{left:0;top:0;width:480px;height:345px;
    background:linear-gradient(90deg,#e9dfd6 0%,#f1ebe6 35%,#f6f2ef 70%,#ffffff 100%)}
  .photo--team{left:19px;top:22px;width:290px;height:178px;
    background:radial-gradient(ellipse at 45% 60%,#e8edf3 0%,#f3f5f8 55%,#ffffff 100%)}

  .brand{position:absolute;display:flex;align-items:center;gap:8px;font-family:"Oswald",sans-serif;font-weight:600;color:var(--navy);line-height:1;text-transform:uppercase;white-space:nowrap}
  .brand__mark{background:var(--navy);flex:none}
  .brand--front{left:430px;top:38px;font-size:25px}
  .brand--front .brand__mark{width:22px;height:22px}
  .brand--back{left:352px;top:44px;font-size:18px}
  .brand--back .brand__mark{width:16px;height:16px}

  .headline{position:absolute;left:428px;font-family:"Oswald",sans-serif;font-weight:700;color:var(--blue);line-height:1;width:240px;text-align:center}
  .headline--grand{top:104px;font-size:80px;letter-spacing:1px}
  .headline--opening{top:180px;font-size:59px;letter-spacing:.5px}
  .date-tag{position:absolute;left:441px;top:239px;width:215px;height:42px;background:var(--navy);color:#fff;font-family:"Lato",sans-serif;font-weight:900;font-size:27px;display:flex;align-items:center;justify-content:center}

  .coupon{position:absolute;text-align:center}
  .coupon__circle{position:absolute;border-radius:50%;background:#fff;border:4px solid var(--blue-mid);display:flex;align-items:center;justify-content:center;font-family:"Oswald",sans-serif;font-weight:700;color:var(--navy)}
  .coupon__pill{position:absolute;background:var(--blue-mid);border:2px solid #fff;border-radius:7px;color:#fff;font-size:11px;line-height:1.2;display:flex;align-items:center;justify-content:center;text-align:center}
  .coupon--front .coupon__circle{left:70px;top:308px;width:86px;height:86px;font-size:38px}
  .coupon--front .coupon__pill{left:58px;top:390px;width:110px;height:30px}
  .coupon--back .coupon__circle{left:43px;top:339px;width:66px;height:66px;font-size:29px}
  .coupon--back .coupon__pill{left:36px;top:398px;width:78px;height:25px;font-size:9px}

  .divider{position:absolute;width:1px;background:rgba(255,255,255,.35)}
  .hours{position:absolute;left:208px;top:383px;color:#fff;font-size:15px;line-height:1.35}
  .walkin{position:absolute;left:433px;top:356px;color:var(--blue-soft);font-size:15px;font-weight:700;letter-spacing:.2px}
  .phone{position:absolute;display:flex;align-items:center;gap:6px;color:#fff;font-weight:900}
  .phone--front{left:433px;top:383px;font-size:25px}
  .phone--back{left:145px;top:378px;font-size:15px}

  .services-title{position:absolute;left:31px;top:203px;font-family:"Oswald",sans-serif;font-weight:600;font-size:15px;line-height:1.2;text-transform:uppercase}
  .services-title__lead{color:var(--blue)}
  .services-title__main{color:var(--navy)}
  .service-list{position:absolute;list-style:none;font-size:10px;font-style:italic;font-weight:700;color:#1e1f3a;white-space:nowrap}
  .service-list li{height:18.5px;display:flex;align-items:center;gap:10px}
  .service-list li::before{content:"";width:7px;height:7px;border-radius:50%;background:var(--blue-mid);flex:none}
  .service-list--a{left:31px;top:238px}
  .service-list--b{left:178px;top:238px}

  .contact-line{position:absolute;left:145px;color:#fff;font-size:10px;display:flex;gap:6px;align-items:flex-start;line-height:1.2}
  .contact-line--addr{top:401px}
  .contact-line--web{top:427px}

  .stamp-box{position:absolute;left:565px;top:36px;width:96px;height:99px;border:1px solid #b5b8bd}
  .address-line{position:absolute;left:391px;width:260px;height:1px;background:#8d9096}
</style>
</head>
<body>

<section class="card card--front" aria-label="Postcard front">
  <div class="photo photo--exam" role="img" aria-label="Photo of a doctor listening to a happy baby with a stethoscope"></div>
  <svg class="layer" width="691" height="470" viewBox="0 0 691 470" aria-hidden="true">
    <path d="M0,292 C150,330 250,352 360,336 C480,318 600,304 691,312 L691,324 C600,318 480,334 360,352 C250,368 150,350 0,310 Z" fill="#4a78c3"/>
    <path d="M440,322 C540,308 620,304 691,310" fill="none" stroke="#9a9ea6" stroke-width="3"/>
    <path d="M0,310 C150,350 250,368 360,352 C480,334 600,318 691,324 L691,442 L0,442 Z" fill="#1c1d5f"/>
    <rect x="0" y="442" width="691" height="28" fill="#4a78c3"/>
  </svg>

  <div class="brand brand--front"><span class="brand__mark"></span>Maple Grove Clinic</div>
  <div class="headline headline--grand">GRAND</div>
  <div class="headline headline--opening">OPENING</div>
  <div class="date-tag">OCTOBER 9TH</div>

  <div class="coupon coupon--front">
    <div class="coupon__circle">$20</div>
    <div class="coupon__pill">gift card with<br>first visit</div>
  </div>
  <div class="divider" style="left:184px;top:375px;height:52px"></div>
  <div class="hours">Monday-Saturday 7am-7pm<br>Sunday : 10am-7pm</div>
  <div class="divider" style="left:420px;top:360px;height:70px"></div>
  <div class="walkin">NO APPOINTMENTS NEEDED</div>
  <div class="phone phone--front">
    <svg width="22" height="22" viewBox="0 0 24 24" aria-hidden="true"><circle cx="12" cy="12" r="10.5" fill="none" stroke="#fff" stroke-width="2"/><path d="M8.6 6.8l1.6-.4 1.2 2.8-1.1 1c.6 1.3 1.5 2.2 2.8 2.8l1-1.1 2.8 1.2-.4 1.6c-.2.7-.9 1.1-1.6 1-3.5-.6-6.1-3.2-6.7-6.7-.1-.7.3-1.4 1-1.6z" fill="#fff"/></svg>
    (555) 014-2870
  </div>
</section>

<section class="card card--back" aria-label="Postcard back">
  <div class="photo photo--team" role="img" aria-label="Photo of a smiling medical team giving thumbs up"></div>
  <svg class="layer" width="690" height="469" viewBox="0 0 690 469" aria-hidden="true">
    <path d="M0,340 C100,342 220,348 336,354 L336,364 C220,358 100,352 0,350 Z" fill="#4a78c3"/>
    <path d="M0,350 C100,352 220,358 336,364 L336,469 L0,469 Z" fill="#1c1d5f"/>
    <path d="M366,0 C336,90 328,180 334,260 C338,340 332,410 322,469 L312,469 C322,410 328,340 324,260 C318,180 326,90 355,0 Z" fill="#4a78c3"/>
    <path d="M372,0 C342,90 334,180 340,260 C344,340 338,410 328,469" fill="none" stroke="#9a9ea6" stroke-width="2"/>
    <path d="M324,260 C328,340 322,410 312,469 L336,469 L336,340 Z" fill="#fff" opacity="0"/>
  </svg>

  <div class="services-title">
    <div class="services-title__lead">We are here for your everyday</div>
    <div class="services-title__main">Healthcare needs:</div>
  </div>
  <ul class="service-list service-list--a">
    <li>Urgent Care</li><li>Medication Refills</li><li>Lab Tests &amp; Vaccinations</li><li>Well Exams</li><li>Health Screenings</li>
  </ul>
  <ul class="service-list service-list--b">
    <li>Pediatrics</li><li>Infections</li><li>Preventive Services</li><li>STD Testing and Treatment</li><li>On-site X-Rays</li>
  </ul>

  <div class="coupon coupon--back">
    <div class="coupon__circle">$20</div>
    <div class="coupon__pill">gift card with<br>first visit</div>
  </div>
  <div class="phone phone--back">
    <svg width="13" height="13" viewBox="0 0 24 24" aria-hidden="true"><circle cx="12" cy="12" r="10.5" fill="none" stroke="#fff" stroke-width="2"/><path d="M8.6 6.8l1.6-.4 1.2 2.8-1.1 1c.6 1.3 1.5 2.2 2.8 2.8l1-1.1 2.8 1.2-.4 1.6c-.2.7-.9 1.1-1.6 1-3.5-.6-6.1-3.2-6.7-6.7-.1-.7.3-1.4 1-1.6z" fill="#fff"/></svg>
    (555) 014-2870
  </div>
  <div class="contact-line contact-line--addr">
    <svg width="10" height="10" viewBox="0 0 24 24" aria-hidden="true"><path d="M12 3L2 12h3v9h5v-6h4v6h5v-9h3z" fill="#fff"/></svg>
    <span>218 Harbor Lane<br>Fairview, Virginia 23000</span>
  </div>
  <div class="contact-line contact-line--web">
    <svg width="10" height="10" viewBox="0 0 24 24" aria-hidden="true"><circle cx="12" cy="12" r="10" fill="none" stroke="#fff" stroke-width="2"/><path d="M2 12h20M12 2c3 3 3 17 0 20M12 2c-3 3-3 17 0 20" fill="none" stroke="#fff" stroke-width="1.5"/></svg>
    <span>www.maplegroveclinicplus.example</span>
  </div>

  <div class="brand brand--back"><span class="brand__mark"></span>Maple Grove Clinic</div>
  <div class="stamp-box"></div>
  <div class="address-line" style="top:231px"></div>
  <div class="address-line" style="top:279px"></div>
  <div class="address-line" style="top:328px"></div>
</section>

</body>
</html>
```